Walk Bright through the Seasons: 52 Weeks to a Year of Courage and Calm

This is a non-fiction, self-help book. The first edition was published a decade ago, and it needs a new design. Nothing too literal (no actual hearts on the cover) but something inspirational or perhaps something quite plain. The current cover is below for reference, but I DO NOT want something similar to that. It is outdated.

The cover must include:

1. Title: Walk Bright through the Seasons
2. Subtitle: 52 Weeks to a Year of Courage and Calm
3. Author Name: Tobin Wells

It should also have plenty of "white space" in other words the fonts shouldnt be so big that they take up the whole cover.

Dimensions: 9" x 6.25"

Target Market(s)

adults interested in personal development

Font styles to use
Serif
Script

Colors

Designer to choose colors to be used in the design.

Requirements
Must have
• Classic look and feel. The current design is too busy. I have included examples of the style I like below. I'm open to a singular graphic/photo but nothing more than that. Probably plain text is best.
• Please look at the samples I have included of best-selling books in the genre that I like. The cover should be modeled after these.

```html
<!DOCTYPE html>
<html lang="en">
<head>
<meta charset="utf-8">
<title>Walk Bright through the Seasons — Cover</title>
<link rel="stylesheet" href="https://fonts.googleapis.com/css2?family=Tinos:wght@400&display=swap">
<style>
  :root {
    --backdrop: #b3a9a7;
    --paper: #f3f3f3;
    --ink: #141414;
    --accent: #b5565a;
  }
  html, body {
    margin: 0;
    padding: 0;
    width: 1200px;
    height: 1054px;
    overflow: hidden;
    background: var(--backdrop);
  }
  .canvas {
    position: relative;
    width: 1200px;
    height: 1054px;
    font-family: "Tinos", "Times New Roman", serif;
    color: var(--ink);
  }
  .front-cover {
    position: absolute;
    left: 366px;
    top: 298px;
    width: 334px;
    height: 474px;
    background: var(--paper);
    text-align: center;
  }
  .title-lead {
    position: absolute;
    top: 78px;
    left: 0;
    right: 0;
    font-size: 34px;
    line-height: 1;
  }
  .title-middle {
    position: absolute;
    top: 142px;
    left: 0;
    right: 0;
    font-size: 23px;
    line-height: 1;
  }
  .title-accent {
    position: absolute;
    top: 182px;
    left: 0;
    right: 0;
    font-size: 34px;
    line-height: 1;
    color: var(--accent);
  }
  .subtitle {
    position: absolute;
    top: 242px;
    left: 0;
    right: 0;
    font-size: 13px;
    line-height: 18px;
  }
  .author {
    position: absolute;
    top: 421px;
    left: 0;
    right: 0;
    font-size: 14px;
    line-height: 1;
  }
  .spine {
    position: absolute;
    left: 763px;
    top: 296px;
    width: 49px;
    height: 464px;
    background: var(--paper);
  }
  .spine-title,
  .spine-author {
    position: absolute;
    left: 0;
    width: 49px;
    writing-mode: vertical-rl;
    transform: rotate(180deg);
    display: flex;
    align-items: center;
    white-space: nowrap;
  }
  .spine-title {
    bottom: 110px;
    height: 344px;
    justify-content: flex-start;
    font-size: 20px;
  }
  .spine-title .big { font-size: 27px; }
  .spine-title .accent { color: var(--accent); }
  .spine-author {
    bottom: 18px;
    height: 76px;
    font-size: 13px;
  }
</style>
</head>
<body>
  <main class="canvas">
    <section class="front-cover">
      <div class="title-lead">Walk</div>
      <div class="title-middle">Bright through the</div>
      <div class="title-accent">Seasons</div>
      <div class="subtitle">52 Weeks to a Year of Courage<br>and Calm</div>
      <div class="author">Tobin Wells</div>
    </section>
    <section class="spine">
      <div class="spine-title"><span class="big">Walk</span>&nbsp;Bright through the&nbsp;<span class="big accent">Seasons</span></div>
      <div class="spine-author">Tobin Wells</div>
    </section>
  </main>
</body>
</html>
```